Demo Screens Needed for Recruiting with AI App

We are in the process of raising money for our startup called KelvoraLink. We need demos to show investors what we're trying to do with images. We really love the simplicity and modern look of the Pivlo App and want something similar. We will have the "swipe" functionality similar to Flarvi as well. The sample images I've attached are only for caregivers but long term this will be for all industries. There will also be a rewards page for loyalty membership. The current landing page is www.kelvoralink-demo.com. That will show you the color scheme and logo.

```html
<!DOCTYPE html>
<html lang="en">
<head>
<meta charset="utf-8">
<title>KelvoraLink – App Screens</title>
<link href="https://fonts.googleapis.com/css2?family=Manrope:wght@400;500;600;700;800&display=swap" rel="stylesheet">
<style>
  :root {
    --canvas: #333333;
    --ink-dark: #121212;
    --ink: #000000;
    --white: #ffffff;
    --violet: #7c3aed;
    --violet-soft: #8b5cf6;
    --muted: #b5b5b5;
    --chip: #2a2a2a;
    --pill-light: #f0f0f0;
    --red: #e5212b;
    --sky: #4aa3f0;
  }
  * { box-sizing: border-box; margin: 0; padding: 0; }
  html, body { width: 1181px; height: 1200px; overflow: hidden; }
  body {
    background: var(--canvas);
    font-family: "Manrope", sans-serif;
    position: relative;
  }
  .screen {
    position: absolute;
    top: 42px;
    width: 515px;
    height: 1115px;
    border-radius: 30px;
    overflow: hidden;
  }
  .screen--welcome {
    left: 42px;
    background: radial-gradient(ellipse 90% 45% at 50% 8%, #2e0f55 0%, #1b0c33 45%, var(--ink-dark) 80%);
    color: var(--white);
  }
  .screen--discover { left: 624px; background: var(--white); color: var(--ink); }

  .status-bar {
    position: absolute; top: 18px; left: 0; right: 0; height: 32px;
    display: flex; align-items: center; justify-content: space-between;
    padding: 0 34px 0 62px;
    font-weight: 700; font-size: 21px;
  }
  .status-icons { display: flex; gap: 8px; align-items: center; }

  .brand {
    position: absolute; left: 20px; top: 72px;
    font-weight: 800; font-size: 30px; letter-spacing: 0.5px;
  }
  .photo-card { position: absolute; border-radius: 34px; }
  .photo-card--one {
    left: 40px; top: 189px; width: 225px; height: 284px;
    transform: rotate(-3deg);
    background: linear-gradient(170deg, #b9cbd4 0%, #8f9c93 45%, #3e2d2f 75%, #5b4a40 100%);
  }
  .photo-card--two {
    left: 235px; top: 251px; width: 238px; height: 288px;
    transform: rotate(4deg);
    background: linear-gradient(160deg, #e6e6e4 0%, #cfcac3 40%, #8a7a6e 70%, #3a3432 100%);
  }
  .headline {
    position: absolute; left: 20px; top: 610px;
    font-weight: 600; font-size: 63px; line-height: 71px; letter-spacing: -0.5px;
  }
  .headline .accent { color: var(--violet-soft); }
  .cta {
    position: absolute; left: 20px; top: 937px; width: 476px; height: 58px;
    border-radius: 29px; background: var(--white);
    display: flex; align-items: center; justify-content: center;
    color: var(--violet); font-weight: 600; font-size: 18px;
  }
  .sign-in-note {
    position: absolute; left: 0; right: 0; top: 1022px; text-align: center;
    color: var(--muted); font-size: 18px; font-weight: 500;
  }
  .sign-in-note strong { color: var(--white); font-weight: 600; }

  .location-pill {
    position: absolute; left: 20px; top: 70px; height: 42px; padding: 0 16px 0 12px;
    border-radius: 21px; background: var(--pill-light);
    display: flex; align-items: center; gap: 6px;
    font-size: 15px; font-weight: 500;
  }
  .filter-button { position: absolute; left: 464px; top: 78px; }
  .profile-card {
    position: absolute; left: 20px; top: 120px; width: 476px; height: 845px;
    border-radius: 30px; overflow: hidden;
    background: linear-gradient(180deg, #5f7150 0%, #44583c 30%, #3a4431 55%, #262a22 75%, #050505 100%);
  }
  .photo-fill { position: absolute; inset: 0; }
  .profile-card .veil {
    position: absolute; inset: 0;
    background: linear-gradient(180deg, transparent 55%, rgba(0,0,0,0.85) 100%);
  }
  .profile-info { position: absolute; left: 21px; top: 650px; color: var(--white); }
  .profile-name { font-size: 32px; font-weight: 600; }
  .profile-name span { font-weight: 400; }
  .profile-place { margin-top: 8px; font-size: 16px; display: flex; align-items: center; gap: 6px; }
  .profile-tags { margin-top: 16px; display: flex; gap: 12px; }
  .tag {
    height: 40px; padding: 0 20px; border-radius: 20px; background: rgba(50,50,50,0.85);
    display: flex; align-items: center; gap: 6px; font-size: 15px;
  }
  .action {
    position: absolute; border-radius: 50%; background: var(--chip);
    display: flex; align-items: center; justify-content: center;
    transform: translate(-50%, -50%); top: 970px;
  }
  .action--big { width: 79px; height: 79px; }
  .action--small { width: 71px; height: 71px; }
  .tab-bar .tab { position: absolute; top: 1049px; transform: translate(-50%, -50%); }
  .tab-home { font-weight: 800; font-size: 38px; line-height: 1; color: var(--violet); }
</style>
</head>
<body>

<section class="screen screen--welcome">
  <div class="status-bar">
    <span>9:41</span>
    <span class="status-icons">
      <svg width="26" height="16" viewBox="0 0 26 16" fill="#fff"><rect x="0" y="11" width="4" height="5" rx="1"/><rect x="7" y="8" width="4" height="8" rx="1"/><rect x="14" y="4" width="4" height="12" rx="1"/><rect x="21" y="0" width="4" height="16" rx="1"/></svg>
      <svg width="22" height="16" viewBox="0 0 22 16" fill="none" stroke="#fff" stroke-width="2.6" stroke-linecap="round"><path d="M2 5.5a13 13 0 0 1 18 0"/><path d="M5.5 9a8 8 0 0 1 11 0"/><circle cx="11" cy="13" r="1.6" fill="#fff" stroke="none"/></svg>
      <svg width="32" height="16" viewBox="0 0 32 16"><rect x="1" y="1" width="26" height="14" rx="4" fill="none" stroke="#fff" stroke-width="1.6"/><rect x="4" y="4" width="20" height="8" rx="2" fill="#fff"/><rect x="29" y="5" width="2" height="6" rx="1" fill="#fff"/></svg>
    </span>
  </div>

  <div class="brand">KELVORALINK</div>

  <div class="photo-card photo-card--one" role="img" aria-label="Photo of a young man with curly hair and glasses outdoors"></div>
  <div class="photo-card photo-card--two" role="img" aria-label="Photo of a young woman with long dark hair leaning on a railing"></div>

  <h1 class="headline">
    <span class="accent">Unlocking</span><br>the Power Of<br>Meaningful<br>Connections
  </h1>

  <div class="cta">Create Account</div>
  <p class="sign-in-note">Already have an account? <strong>Sign In</strong></p>
</section>

<section class="screen screen--discover">
  <div class="status-bar">
    <span>9:41</span>
    <span class="status-icons">
      <svg width="26" height="16" viewBox="0 0 26 16" fill="#000"><rect x="0" y="11" width="4" height="5" rx="1"/><rect x="7" y="8" width="4" height="8" rx="1"/><rect x="14" y="4" width="4" height="12" rx="1"/><rect x="21" y="0" width="4" height="16" rx="1"/></svg>
      <svg width="22" height="16" viewBox="0 0 22 16" fill="none" stroke="#000" stroke-width="2.6" stroke-linecap="round"><path d="M2 5.5a13 13 0 0 1 18 0"/><path d="M5.5 9a8 8 0 0 1 11 0"/><circle cx="11" cy="13" r="1.6" fill="#000" stroke="none"/></svg>
      <svg width="32" height="16" viewBox="0 0 32 16"><rect x="1" y="1" width="26" height="14" rx="4" fill="none" stroke="#000" stroke-width="1.6"/><rect x="4" y="4" width="20" height="8" rx="2" fill="#000"/><rect x="29" y="5" width="2" height="6" rx="1" fill="#000"/></svg>
    </span>
  </div>

  <div class="location-pill">
    <svg width="18" height="22" viewBox="0 0 18 22"><path d="M9 1a7.5 7.5 0 0 0-7.5 7.5C1.5 14 9 21 9 21s7.5-7 7.5-12.5A7.5 7.5 0 0 0 9 1z" fill="#000"/><circle cx="9" cy="8.5" r="2.6" fill="#f0f0f0"/></svg>
    Palo Alto - 15mi
  </div>
  <svg class="filter-button" width="28" height="24" viewBox="0 0 28 24" stroke="#000" stroke-width="2.6" stroke-linecap="round"><line x1="2" y1="4" x2="26" y2="4"/><line x1="6" y1="12" x2="22" y2="12"/><line x1="10" y1="20" x2="18" y2="20"/></svg>

  <div class="profile-card">
    <div class="photo-fill" role="img" aria-label="Photo of a smiling woman holding a tennis racket on a court"></div>
    <div class="veil"></div>
    <div class="profile-info">
      <div class="profile-name">Rena K, <span>24</span></div>
      <div class="profile-place">
        <svg width="13" height="16" viewBox="0 0 18 22"><path d="M9 1a7.5 7.5 0 0 0-7.5 7.5C1.5 14 9 21 9 21s7.5-7 7.5-12.5A7.5 7.5 0 0 0 9 1z" fill="#fff"/><circle cx="9" cy="8.5" r="2.6" fill="#222"/></svg>
        Palo Alto, CA
      </div>
      <div class="profile-tags">
        <span class="tag">From $25/hr</span>
        <span class="tag">
          <svg width="15" height="15" viewBox="0 0 24 24" fill="#fff"><path d="M12 2l3 6.5 7 .8-5.2 4.8 1.4 7L12 17.6 5.8 21.1l1.4-7L2 9.3l7-.8z"/></svg>
          4.5/5 (7)
        </span>
      </div>
    </div>
  </div>

  <div class="action action--small" style="left:115px;">
    <svg width="32" height="28" viewBox="0 0 32 28" fill="none" stroke="#6b6b6b" stroke-width="3" stroke-linecap="round" stroke-linejoin="round"><path d="M9 4L3 10l6 6"/><path d="M3 10h17a8 8 0 0 1 0 16h-8"/></svg>
  </div>
  <div class="action action--big" style="left:206px;">
    <svg width="30" height="30" viewBox="0 0 30 30" stroke="#e5212b" stroke-width="4.5" stroke-linecap="round"><line x1="4" y1="4" x2="26" y2="26"/><line x1="26" y1="4" x2="4" y2="26"/></svg>
  </div>
  <div class="action action--big" style="left:308px;">
    <svg width="36" height="32" viewBox="0 0 24 22" fill="#8b5cf6"><path d="M12 21s-9.5-6-9.5-12.2A5.3 5.3 0 0 1 12 5.3a5.3 5.3 0 0 1 9.5 3.5C21.5 15 12 21 12 21z"/></svg>
  </div>
  <div class="action action--small" style="left:404px;">
    <svg width="32" height="32" viewBox="0 0 24 24" fill="#4aa3f0"><path d="M12 1c.6 5.6 5.4 10.4 11 11-5.6.6-10.4 5.4-11 11-.6-5.6-5.4-10.4-11-11C6.6 11.4 11.4 6.6 12 1z"/></svg>
  </div>

  <nav class="tab-bar">
    <span class="tab tab-home" style="left:61px;">K</span>
    <svg class="tab" style="left:160px;" width="34" height="34" viewBox="0 0 34 34" fill="#000"><rect x="1" y="1" width="14" height="14" rx="3"/><rect x="19" y="1" width="14" height="14" rx="3"/><rect x="1" y="19" width="14" height="14" rx="3"/><rect x="19" y="19" width="14" height="14" rx="3"/></svg>
    <svg class="tab" style="left:256px;" width="36" height="36" viewBox="0 0 24 24" fill="#000"><path d="M12 1c.6 5.6 5.4 10.4 11 11-5.6.6-10.4 5.4-11 11-.6-5.6-5.4-10.4-11-11C6.6 11.4 11.4 6.6 12 1z"/></svg>
    <svg class="tab" style="left:354px;" width="36" height="36" viewBox="0 0 36 36" fill="#000"><path d="M6 3h24a4 4 0 0 1 4 4v16a4 4 0 0 1-4 4H14l-8 7v-7a4 4 0 0 1-4-4V7a4 4 0 0 1 4-4z"/></svg>
    <svg class="tab" style="left:452px;" width="34" height="34" viewBox="0 0 34 34" fill="#000"><circle cx="17" cy="9" r="8"/><path d="M2 33c0-8 6.5-13 15-13s15 5 15 13z"/></svg>
  </nav>
</section>

</body>
</html>
```